Marlene Business Card

My wife is going to start her own business with renting holiday appartments to tourists. She needs a design for a new business card... and a new web site.
Look at Roomvesta "Ruhezeit am Birkenteich"

Target Market(s)

Give business card to prospects at any situation

Contact Information for Business Card

not sure what this means

Font styles to use
Script

Colors
fec41a
fee18a

Requirements
Must have
• My wife's handwriting is difficult to read:
Entspannen - Loslassen - Auftanken
Marlene & der Birkenteich
Urlaub an einem besonderen Ort
Marlene Brökel
Gartenpfad 7
17489 Alt Medow
info@marlene-broekel.de
www.birkenteich.net
Nice to have
• Beige background
Font like handwriting

```html
<!DOCTYPE html>
<html lang="de">
<head>
<meta charset="utf-8">
<title>Marlene &amp; der Birkenteich – Visitenkarte</title>
<link rel="stylesheet" href="https://fonts.googleapis.com/css2?family=Pinyon+Script&family=Lugrasimo&display=swap">
<style>
  :root {
    --page-bg: #2e2e2e;
    --gold: #fec41a;
    --gold-pale: #fee18a;
    --gold-light: #fbeaa6;
    --band: #a8864a;
    --ink: #1d1a12;
    --photo-light: #e0a126;
    --photo-mid: #b56d12;
    --photo-dark: #3a2208;
    --white: #ffffff;
  }
  * { margin: 0; padding: 0; box-sizing: border-box; }
  html, body { width: 1200px; height: 900px; overflow: hidden; }
  body {
    background: var(--page-bg);
    display: flex;
    flex-direction: column;
    align-items: center;
    justify-content: center;
    gap: 40px;
  }
  .card {
    position: relative;
    width: 700px;
    height: 400px;
    overflow: hidden;
    box-shadow: 0 10px 30px rgba(0,0,0,.45);
  }
  .card-art { position: absolute; inset: 0; }
  .script { font-family: "Pinyon Script", cursive; color: var(--ink); }
  .calli { font-family: "Lugrasimo", cursive; color: var(--ink); }

  /* Back side */
  .tagline {
    position: absolute; top: 28px; left: 0; width: 100%;
    text-align: center; font-size: 46px;
  }
  .website {
    position: absolute; top: 96px; left: 0; width: 100%;
    text-align: center; font-size: 34px; letter-spacing: 2px;
  }
  .contact-list {
    position: absolute; right: 36px; top: 178px;
    list-style: none; text-align: right; font-size: 19px; line-height: 36px;
  }
  .contact-list li { display: flex; justify-content: flex-end; align-items: center; gap: 8px; }
  .contact-list svg { width: 18px; height: 18px; fill: var(--ink); }
  .holder-name {
    position: absolute; left: 40px; bottom: 22px; font-size: 20px;
  }

  /* Front side */
  .brand-title {
    position: absolute; left: 40px; top: 150px; font-size: 58px;
  }
  .claim {
    position: absolute; right: 40px; bottom: 70px;
    font-size: 50px; color: var(--white);
  }
</style>
</head>
<body>

<section class="card card-back">
  <svg class="card-art" viewBox="0 0 700 400" preserveAspectRatio="none">
    <defs>
      <linearGradient id="backGold" x1="0" y1="0" x2="1" y2="1">
        <stop offset="0" stop-color="var(--gold-pale)"/>
        <stop offset=".5" stop-color="var(--gold)"/>
        <stop offset="1" stop-color="var(--gold-pale)"/>
      </linearGradient>
    </defs>
    <rect width="700" height="400" fill="url(#backGold)"/>
    <path d="M0,335 C220,335 300,320 420,220 S620,100 700,95 L700,400 L0,400 Z" fill="var(--gold-light)"/>
    <path d="M0,335 C220,335 300,320 420,220 S620,100 700,95" fill="none" stroke="var(--band)" stroke-width="9" stroke-opacity=".8"/>
  </svg>
  <p class="tagline script">Entspannen - Loslassen - Auftanken</p>
  <p class="website calli">www.birkenteich.net</p>
  <ul class="contact-list calli">
    <li>+49 1520 4417 309
      <svg viewBox="0 0 24 24"><path d="M6.6 10.8a15 15 0 0 0 6.6 6.6l2.2-2.2a1 1 0 0 1 1-.25 11.4 11.4 0 0 0 3.6.6 1 1 0 0 1 1 1V20a1 1 0 0 1-1 1A17 17 0 0 1 3 4a1 1 0 0 1 1-1h3.5a1 1 0 0 1 1 1c0 1.25.2 2.45.6 3.6a1 1 0 0 1-.25 1z"/></svg>
    </li>
    <li>info@marlene-broekel.de
      <svg viewBox="0 0 24 24"><path d="M3 5h18a1 1 0 0 1 1 1v12a1 1 0 0 1-1 1H3a1 1 0 0 1-1-1V6a1 1 0 0 1 1-1zm9 7.5L20 7H4z"/></svg>
    </li>
    <li>Gartenpfad 7, 17489 Alt Medow
      <svg viewBox="0 0 24 24"><path d="M12 2a7 7 0 0 1 7 7c0 5-7 13-7 13S5 14 5 9a7 7 0 0 1 7-7zm0 4.5A2.5 2.5 0 1 0 12 11.5 2.5 2.5 0 0 0 12 6.5z"/></svg>
    </li>
  </ul>
  <p class="holder-name calli">Marlene Brökel</p>
</section>

<section class="card card-front">
  <svg class="card-art" viewBox="0 0 700 400" preserveAspectRatio="none">
    <defs>
      <linearGradient id="frontGold" x1="0" y1="0" x2="1" y2="0">
        <stop offset="0" stop-color="var(--gold-pale)"/>
        <stop offset=".55" stop-color="var(--gold)"/>
        <stop offset="1" stop-color="var(--gold-pale)"/>
      </linearGradient>
      <linearGradient id="sunsetTones" x1="0" y1="0" x2="0" y2="1">
        <stop offset="0" stop-color="var(--photo-light)"/>
        <stop offset=".55" stop-color="var(--photo-mid)"/>
        <stop offset="1" stop-color="var(--photo-dark)"/>
      </linearGradient>
    </defs>
    <rect width="700" height="400" fill="url(#frontGold)"/>
    <path role="img" aria-label="Foto: Sonnenuntergang über Baumsilhouetten am Teich"
          d="M0,255 C180,275 300,250 420,160 S610,45 700,40 L700,400 L0,400 Z" fill="url(#sunsetTones)"/>
    <path d="M0,255 C180,275 300,250 420,160 S610,45 700,40" fill="none" stroke="var(--band)" stroke-width="10" stroke-opacity=".75"/>
  </svg>
  <h1 class="brand-title script">Marlene &amp; der Birkenteich</h1>
  <p class="claim script">Urlaub an einem besonderen Ort</p>
</section>

</body>
</html>
```